Velvet Harbor small batch hot sauce label project

I am launching a line of small batch sauces (hot sauces, bbq sauces) and I need a label for my bottles. I have a logo that I like, I'm not completely married to it but It is a good logo. I would like the name of my business and the name of the sauce on the label. Something fun, edgy that would make you want to pick it up off the shelf.

Target Market(s)

Milennials, food bloggers, stay at home moms who want to amp up their dishes with a really good sauce

Industry/Entity Type

Cooking

Requirements
Must have
• I am open to interpretation
Nice to have
• Maybe a bomb cloud since I want to go in the sauce bomb direction.

```html
<!DOCTYPE html>
<html lang="en">
<head>
<meta charset="utf-8">
<title>Velvet Harbor – Garlic &amp; Harissa Hot Sauce Label</title>
<link href="https://fonts.googleapis.com/css2?family=Lilita+One&display=swap" rel="stylesheet">
<style>
  :root {
    --paper: #ffffff;
    --peach-pale: #fde9dc;
    --sauce-red: #c03434;
    --title-red: #c2313a;
    --ink-brown: #3a2222;
    --hot-orange: #f28a2e;
    --mustard: #f2a33a;
    --cloud-cream: #fdf0cf;
    --cloud-sand: #f7dca8;
    --cloud-amber: #eba24e;
  }
  * { margin: 0; padding: 0; box-sizing: border-box; }
  html, body {
    width: 1200px; height: 2490px; overflow: hidden;
    background: var(--paper);
  }
  .canvas { position: relative; width: 1200px; height: 2490px; }

  /* Neck label */
  .neck-label {
    position: absolute; left: 136px; top: 0; width: 928px; height: 351px;
    overflow: hidden;
  }
  .neck-label .pattern {
    position: absolute; inset: 0 0 84px 0;
    background: linear-gradient(180deg, var(--peach-pale), #fff5ee);
  }
  .neck-label .stripe-band {
    position: absolute; left: 0; right: 0; bottom: 0; height: 84px;
    background: var(--sauce-red);
  }
  .brand {
    position: absolute; left: 0; right: 0;
    display: flex; align-items: center; justify-content: center; gap: 16px;
    font-family: 'Lilita One', sans-serif;
    text-transform: uppercase;
    color: var(--ink-brown);
    letter-spacing: 4px;
    line-height: 1;
  }
  .brand .mark { background: var(--ink-brown); flex: none; }
  .neck-label .brand { top: 122px; font-size: 44px; }
  .neck-label .brand .mark { width: 40px; height: 40px; }

  /* Main label */
  .main-label {
    position: absolute; left: 0; top: 573px; width: 1200px; height: 1885px;
    overflow: hidden;
  }
  .main-label .pattern {
    position: absolute; inset: 0;
    background: linear-gradient(180deg, var(--peach-pale) 0%, #fff7f1 50%, var(--peach-pale) 100%);
  }
  .flavour {
    position: absolute; left: 0; right: 0; top: 62px;
    text-align: center;
    font-family: 'Lilita One', sans-serif;
    font-weight: 400;
    text-transform: uppercase;
    font-size: 88px; line-height: 1; letter-spacing: 1px;
    color: var(--title-red);
    text-shadow: 5px 5px 0 var(--ink-brown);
  }
  .hot-word {
    position: absolute; left: 290px; top: 176px; width: 600px; height: 230px;
  }
  .hot-word text {
    font-family: 'Lilita One', sans-serif;
    font-size: 290px;
  }
  .sauce-plate {
    position: absolute; left: 354px; top: 400px; width: 470px; height: 152px;
  }
  .sauce-plate span {
    position: absolute; inset: 0;
    display: flex; align-items: center; justify-content: center;
    font-family: 'Lilita One', sans-serif;
    font-size: 72px; letter-spacing: 2px; line-height: 1;
    color: var(--mustard);
  }
  .bomb-cloud {
    position: absolute; left: 250px; top: 585px; width: 590px; height: 820px;
    background: radial-gradient(ellipse 62% 55% at 50% 32%,
      var(--cloud-cream) 0%, var(--cloud-sand) 45%, var(--cloud-amber) 80%, #d9822f 100%);
    border-radius: 50% 50% 44% 44% / 38% 38% 30% 30%;
  }
  .main-label .brand { top: 1536px; font-size: 46px; }
  .main-label .brand .mark { width: 42px; height: 42px; }
  .bottom-band {
    position: absolute; left: 0; right: 0; bottom: 0; height: 148px;
    background: var(--sauce-red);
  }
  .heat-gauge {
    position: absolute; left: 455px; top: 1600px; width: 244px; height: 244px;
  }
</style>
</head>
<body>
<div class="canvas">

  <section class="neck-label">
    <div class="pattern" role="img" aria-label="Pale peach zigzag chevron pattern"></div>
    <div class="brand"><span class="mark"></span>Velvet Harbor</div>
    <div class="stripe-band" role="img" aria-label="Red band with diagonal white stripes"></div>
  </section>

  <section class="main-label">
    <div class="pattern" role="img" aria-label="Pale peach zigzag chevron pattern"></div>

    <h1 class="flavour">Garlic &amp; Harissa</h1>

    <svg class="hot-word" viewBox="0 0 600 230" aria-label="Hot">
      <defs>
        <linearGradient id="hotFill" x1="0" y1="0" x2="0" y2="1">
          <stop offset="0" stop-color="#f7a25a"/>
          <stop offset="1" stop-color="#ffffff"/>
        </linearGradient>
      </defs>
      <text x="18" y="222" textLength="548" lengthAdjust="spacingAndGlyphs" fill="#3a2222">HOT</text>
      <text x="8" y="212" textLength="548" lengthAdjust="spacingAndGlyphs" fill="url(#hotFill)" stroke="#f28a2e" stroke-width="7" paint-order="stroke">HOT</text>
    </svg>

    <div class="sauce-plate">
      <svg width="470" height="152" viewBox="0 0 470 152" aria-hidden="true">
        <polygon points="0,0 470,28 436,152 28,140" fill="#5a2a2a"/>
        <polygon points="10,8 462,32 430,142 34,132" fill="#2f2424"/>
      </svg>
      <span>SAUCE</span>
    </div>

    <div class="bomb-cloud" role="img" aria-label="Cartoon mushroom cloud explosion in cream, brown and orange"></div>

    <div class="brand"><span class="mark"></span>Velvet Harbor</div>

    <div class="bottom-band"></div>

    <svg class="heat-gauge" viewBox="0 0 244 244" role="img" aria-label="Round heat level gauge with flame">
      <circle cx="122" cy="122" r="120" fill="#2a2020"/>
      <circle cx="122" cy="122" r="104" fill="none" stroke="#c03434" stroke-width="10"/>
      <circle cx="122" cy="122" r="88" fill="#3a2222"/>
      <circle cx="122" cy="134" r="40" fill="#e2452f"/>
    </svg>
  </section>

</div>
</body>
</html>
```